Poster Design For Obstacle Run

Design a poster for the Crow Ridge Obstacle run.
Text: Crow Ridge Obstacle Run. May 12th, 2018. Sittard. www.crowridgedash.nl. I have added a lot of pictures.
Furthermore, the logo should be included. As an example I included a poster from the ironbark race that we really like (ironbark team challenge) and also. Feel free to take a look at our website for inspiration: www.crowridgedash.nl

```html
<!DOCTYPE html>
<html lang="en">
<head>
<meta charset="utf-8">
<title>Crow Ridge Obstacle Run – Poster</title>
<link rel="stylesheet" href="https://fonts.googleapis.com/css2?family=Oswald:wght@500;600;700&display=swap">
<style>
  :root {
    --backdrop: #e9e6e2;
    --poster-black: #141414;
    --poster-dark: #1f1f1f;
    --splash-orange: #ef5a24;
    --splash-red: #e32a1f;
    --mud-brown: #6b4a3a;
    --white: #ffffff;
  }
  * { box-sizing: border-box; margin: 0; padding: 0; }
  html, body { width: 1200px; height: 1200px; overflow: hidden; }
  body {
    background: var(--backdrop);
    position: relative;
    font-family: "Oswald", "Arial Narrow", sans-serif;
  }
  .poster {
    position: absolute;
    left: 225px; top: 70px;
    width: 750px; height: 1060px;
    overflow: hidden;
    background: radial-gradient(ellipse at 60% 70%, var(--poster-dark), var(--poster-black) 75%);
    box-shadow: 0 6px 24px rgba(0,0,0,0.25);
  }
  .hero-image {
    position: absolute;
    left: 0; top: 0;
    width: 750px; height: 640px;
    background:
      radial-gradient(ellipse 40% 42% at 80% 50%, rgba(107,74,58,0.95), rgba(107,74,58,0) 100%),
      radial-gradient(ellipse 42% 36% at 48% 28%, var(--splash-red), rgba(227,42,31,0) 100%),
      radial-gradient(ellipse 60% 55% at 38% 42%, var(--splash-orange), rgba(239,90,36,0) 100%),
      linear-gradient(to bottom, rgba(20,20,20,0) 70%, var(--poster-black) 100%);
  }
  .headline { margin: 0; font-weight: inherit; }
  .headline__line,
  .headline__date {
    position: absolute;
    display: block;
    line-height: 1;
    white-space: nowrap;
    text-transform: uppercase;
    transform-origin: 0 100%;
    transform: rotate(-24deg);
  }
  .headline__line {
    color: var(--white);
    font-weight: 700;
    -webkit-text-stroke: 20px #000;
    paint-order: stroke fill;
  }
  .headline__line--first { left: 38px; top: 620px; font-size: 92px; }
  .headline__line--second { left: 150px; top: 688px; font-size: 96px; }
  .headline__date {
    left: 202px; top: 810px;
    color: var(--splash-orange);
    font-weight: 600;
    font-size: 54px;
  }
  .footer-rule {
    position: absolute;
    left: 33px;
    width: 373px; height: 12px;
    background: var(--white);
  }
  .footer-rule--top { top: 934px; }
  .footer-rule--bottom { top: 1016px; }
  .footer-url {
    position: absolute;
    left: 33px; top: 952px;
    color: var(--splash-orange);
    font-weight: 500;
    font-size: 38px;
    line-height: 56px;
    letter-spacing: -0.5px;
    text-transform: uppercase;
    white-space: nowrap;
  }
  .event-mark {
    position: absolute;
    left: 430px; top: 950px;
    display: flex;
    align-items: center;
    gap: 12px;
  }
  .event-mark__square {
    width: 26px; height: 26px;
    background: var(--splash-orange);
  }
  .event-mark__name {
    color: var(--splash-orange);
    font-weight: 600;
    font-size: 34px;
    line-height: 1.05;
    text-transform: uppercase;
    white-space: nowrap;
  }
</style>
</head>
<body>
  <main class="poster">
    <div class="hero-image" role="img" aria-label="Mud-covered arm gripping a thick rope over bright orange and red paint splatter"></div>

    <h1 class="headline">
      <span class="headline__line headline__line--first">Crow Ridge</span>
      <span class="headline__line headline__line--second">Obstacle Run</span>
      <span class="headline__date">May 12th, 2018 Sittard</span>
    </h1>

    <div class="footer-rule footer-rule--top"></div>
    <p class="footer-url">www.crowridgedash.nl.</p>
    <div class="footer-rule footer-rule--bottom"></div>

    <div class="event-mark">
      <span class="event-mark__square"></span>
      <span class="event-mark__name">Crow Ridge<br>Obstacle Run</span>
    </div>
  </main>
</body>
</html>
```